Retail Jewelry Business Card Design Project

We are in need of a new business card design for a retail jewelry store. This store is in the business of fine jewelry including but not specific to bridal jewelry, diamonds, designer jewelry and watches.

This store has been in business for 20 years but continues to strive for a modern professional appeal. The main colors use for this business are a royal blue, white and silver.

Target Market(s)

Target market is ages 18-50

Industry/Entity Type

Jewelry

Requirements
Must have
• Sales Person Name
Sales Person Email Address

Store Address
Store Phone
Website

Standard business card size. No odd shapes or sizes.
Nice to have
• Overall modern feel for card.

We have thought that a design with a nice feature of the logo on the back of the card would be nice but open to ideas.
Should not have
• No specific images of jewelry should be used.

```html
<!DOCTYPE html>
<html lang="en">
<head>
<meta charset="utf-8">
<title>Ashby Marwood Fine Jewelry – Business Card</title>
<link rel="stylesheet" href="https://fonts.googleapis.com/css2?family=Cormorant+Garamond:wght@400;600&family=Pinyon+Script&display=swap">
<style>
  :root {
    --royal-blue: #2e3192;
    --blue-soft: #4a4fae;
    --address-blue: #8c90ba;
    --card-white: #ffffff;
    --card-silver: #d9d9bf;
    --card-edge: #b9bcb6;
    --backdrop: #e9e9ec;
  }
  * { margin: 0; padding: 0; box-sizing: border-box; }
  html, body {
    width: 1200px;
    height: 900px;
    overflow: hidden;
    background: var(--backdrop);
  }
  .canvas {
    position: relative;
    width: 1200px;
    height: 900px;
  }
  .business-card {
    position: absolute;
    left: 233px;
    top: 238px;
    width: 744px;
    height: 428px;
    border-radius: 26px;
    overflow: hidden;
    border: 1px solid var(--card-edge);
    background:
      radial-gradient(ellipse 60% 55% at 100% 0%, var(--card-silver) 0%, rgba(217,217,191,0) 100%),
      radial-gradient(ellipse 55% 40% at 30% 100%, var(--card-silver) 0%, rgba(217,217,191,0) 100%),
      var(--card-white);
  }
  .brand-band {
    position: absolute;
    left: 0;
    top: 0;
    width: 240px;
    height: 100%;
    background: var(--royal-blue);
  }
  .band-mark-area {
    position: absolute;
    left: 50px;
    top: 138px;
    width: 140px;
    height: 140px;
    border-radius: 50%;
    background: radial-gradient(circle, rgba(160,164,220,0.55) 0%, rgba(120,124,200,0.25) 70%, rgba(46,49,146,0) 100%);
  }
  .card-details {
    position: absolute;
    left: 316px;
    top: 0;
    right: 20px;
    height: 100%;
    color: var(--royal-blue);
  }
  .salesperson-name {
    position: absolute;
    top: 134px;
    font-family: "Pinyon Script", cursive;
    font-size: 32px;
    color: var(--royal-blue);
    white-space: nowrap;
  }
  .store-name {
    position: absolute;
    top: 228px;
    width: 330px;
    font-family: "Cormorant Garamond", serif;
    font-weight: 600;
    color: var(--royal-blue);
    text-align: center;
    line-height: 1;
  }
  .store-name .store-title {
    display: block;
    font-size: 50px;
  }
  .store-name .store-trade {
    display: block;
    margin-top: 8px;
    font-size: 20px;
    letter-spacing: 2px;
    text-transform: uppercase;
  }
  .store-address {
    position: absolute;
    top: 352px;
    font-family: "Cormorant Garamond", serif;
    font-weight: 400;
    font-size: 19px;
    line-height: 25px;
    color: var(--address-blue);
    white-space: nowrap;
  }
</style>
</head>
<body>
  <main class="canvas">
    <article class="business-card">
      <div class="brand-band">
        <div class="band-mark-area" role="img" aria-label="Brand emblem area"></div>
      </div>
      <section class="card-details">
        <p class="salesperson-name">Lionel Ashby Marwood</p>
        <h1 class="store-name">
          <span class="store-title">Ashby Marwood</span>
          <span class="store-trade">Fine Jewelry</span>
        </h1>
        <address class="store-address">
          2280 Whitlock Avenue, Bay Harbor,<br>
          FL 32590, www.ashbymarwoodjewelry.com
        </address>
      </section>
    </article>
  </main>
</body>
</html>
```